Vornel Technologies business card design

We need a business card designed with our new logo. it would be great if the card could communicate it is a technology based company.

Target Market(s)

system integrators

Industry/Entity Type

technology, IOT

Contact Information for Business Card

Name, designation, Address, telephone number, email address

Requirements
Must have
• logo and company name
Nice to have
• something to do with technology

```html
<!DOCTYPE html>
<html lang="en">
<head>
<meta charset="utf-8">
<title>Vornel Technologies — Business Card</title>
<link href="https://fonts.googleapis.com/css2?family=Exo+2:wght@600&family=Poppins:wght@300&display=swap" rel="stylesheet">
<style>
  :root {
    --page: #ffffff;
    --card-dark: #191c1c;
    --card-mid: #202424;
    --card-light: #272b2c;
    --brand-orange: #ff7f00;
    --text-light: #f0f0f0;
  }
  * { margin: 0; padding: 0; box-sizing: border-box; }
  html, body {
    width: 1200px; height: 1200px; overflow: hidden;
    background: var(--page);
  }
  .canvas { position: relative; width: 1200px; height: 1200px; }

  .card {
    position: absolute; left: 191px; width: 814px; height: 488px;
    background: linear-gradient(160deg, var(--card-mid) 0%, var(--card-dark) 40%, var(--card-light) 100%);
    overflow: hidden;
  }
  .card--front { top: 131px; }
  .card--back { top: 630px; }

  .wordmark {
    position: absolute; display: flex; align-items: center;
    font-family: "Exo 2", sans-serif; font-weight: 600;
    color: var(--text-light); line-height: 1;
  }
  .wordmark__square { background: var(--brand-orange); flex: none; }
  .wordmark__text { display: flex; flex-direction: column; }
  .wordmark__sub { letter-spacing: 0.42em; }

  .card--front .wordmark { left: 172px; top: 176px; gap: 22px; }
  .card--front .wordmark__square { width: 70px; height: 70px; }
  .card--front .wordmark__name { font-size: 62px; letter-spacing: 0.02em; }
  .card--front .wordmark__sub { font-size: 22px; margin-top: 12px; }

  .card--back .wordmark { left: 76px; top: 72px; gap: 14px; }
  .card--back .wordmark__square { width: 44px; height: 44px; }
  .card--back .wordmark__name { font-size: 38px; letter-spacing: 0.02em; }
  .card--back .wordmark__sub { font-size: 13.5px; margin-top: 8px; }

  .contacts { position: absolute; left: 400px; top: 182px; list-style: none; }
  .contact {
    display: flex; align-items: center; height: 57px; margin-bottom: 5px;
    padding: 0 28px 0 18px; border-radius: 29px;
    background: var(--brand-orange); width: max-content;
    font-family: "Poppins", sans-serif; font-weight: 300;
    font-size: 24px; color: #ffffff; letter-spacing: -0.02em;
  }
  .contact svg { width: 34px; height: 34px; margin-right: 12px; flex: none; }
</style>
</head>
<body>
<div class="canvas">

  <section class="card card--front" role="img" aria-label="Dark charcoal card background with a soft diamond texture">
    <div class="wordmark">
      <span class="wordmark__square"></span>
      <span class="wordmark__text">
        <span class="wordmark__name">VORNEL</span>
        <span class="wordmark__sub">TECHNOLOGIES</span>
      </span>
    </div>
  </section>

  <section class="card card--back" role="img" aria-label="Dark charcoal card background with a soft diamond texture">
    <div class="wordmark">
      <span class="wordmark__square"></span>
      <span class="wordmark__text">
        <span class="wordmark__name">VORNEL</span>
        <span class="wordmark__sub">TECHNOLOGIES</span>
      </span>
    </div>

    <ul class="contacts">
      <li class="contact">
        <svg viewBox="0 0 24 24" aria-hidden="true"><path fill="#fff" d="M12 1.5a7 7 0 0 0-7 7c0 4.6 7 14 7 14s7-9.4 7-14a7 7 0 0 0-7-7zm0 9.8a2.8 2.8 0 1 1 0-5.6 2.8 2.8 0 0 1 0 5.6z"/></svg>
        12 Harbor Lane
      </li>
      <li class="contact">
        <svg viewBox="0 0 24 24" aria-hidden="true" fill="none" stroke="#fff" stroke-width="1.8"><circle cx="12" cy="12" r="9.5" fill="#fff" stroke="none"/><ellipse cx="12" cy="12" rx="4" ry="9.5" stroke="#ff7f00"/><path d="M2.5 12h19M12 2.5v19" stroke="#ff7f00"/></svg>
        www.vornel-tech.com
      </li>
      <li class="contact">
        <svg viewBox="0 0 24 24" aria-hidden="true" fill="none" stroke="#fff" stroke-width="1.6"><rect x="2" y="4.5" width="20" height="15" rx="1.5"/><path d="M3 5.5l9 8 9-8" fill="#fff"/></svg>
        hello@vornel-tech.com
      </li>
      <li class="contact">
        <svg viewBox="0 0 24 24" aria-hidden="true"><path fill="#fff" d="M6.6 2.5c1 0 1.6 1.9 2 3 .3 1-.9 1.8-1.3 2.5.9 2.6 4 5.7 6.6 6.6.6-.4 1.5-1.6 2.5-1.3 1.1.4 3 1 3 2 0 1.6-1.6 3.2-3.2 3.2C10.5 18.5 5.5 13.5 5.5 7.8 5.5 5 5.5 2.5 6.6 2.5z"/></svg>
        0300 555 0142
      </li>
    </ul>
  </section>

</div>
</body>
</html>
```